Website Design for A Nook for Grandpas

Please design and code a new website.
Here are the sites I like best:
http://www.sailbeacon.net/alternate/
http://www.wheelsgiving.net
Please make it similar but look at the competitor site (below) for images and wording. This is NOT a car donation site. It's a senior lead placement site like https://www.eldernestfinder.net. I just like this sites above as a lead generation sites.
Competitor site:
https://www.eldernestfinder.net (use ideas / verbiage from this site)
Updates
Competitor site:

```html
<!DOCTYPE html>
<html lang="en">
<head>
<meta charset="utf-8">
<title>A Nook for Grandpas – Senior Living Advisors</title>
<link href="https://fonts.googleapis.com/css2?family=Exo+2:wght@400;500;600&family=Montserrat:ital,wght@0,400;0,500;0,600;1,400&display=swap" rel="stylesheet">
<style>
:root{
  --blue:#0d2583;
  --red:#e63b2e;
  --ink:#1b1b1b;
  --muted:#555;
  --grey-bg:#f0f1f4;
  --line:#c9c9c9;
  --white:#fff;
  --black:#000;
}
*{box-sizing:border-box;margin:0;padding:0}
html,body{width:1200px;height:2904px;overflow:hidden;background:var(--white)}
body{position:relative;font-family:"Montserrat",sans-serif;color:var(--ink)}
.abs{position:absolute}
.head-font{font-family:"Exo 2",sans-serif}
.red{color:var(--red)}

/* header */
.site-header{left:0;top:0;width:1200px;height:83px;background:var(--white)}
.brand{left:141px;top:14px;color:var(--blue);font-family:"Exo 2",sans-serif;font-size:29px;font-weight:400}
.brand-sub{left:141px;top:50px;width:183px;display:flex;align-items:center;gap:8px;color:var(--red);font-size:11px}
.brand-sub::before,.brand-sub::after{content:"";flex:1;height:1px;background:#555}
.main-nav{left:0;top:83px;width:1200px;height:35px;background:var(--blue)}
.main-nav a{position:absolute;top:0;height:35px;line-height:35px;color:var(--white);font-size:12px;font-weight:500;text-decoration:none}
.main-nav a.active{background:var(--red);padding:0 18px}
.caret{display:inline-block;margin-left:8px;border:5px solid transparent;border-top-color:#fff;border-bottom:0;vertical-align:middle}

.hero{left:0;top:118px;width:1200px;height:354px;background:linear-gradient(90deg,#b9b3ab 0%,#d8d2c9 40%,#9f958a 70%,#786c60 100%)}

/* lead panel */
.lead-panel{left:748px;top:0;width:282px;height:472px;background:var(--red);color:var(--white)}
.help{left:22px;top:18px;display:flex;gap:10px;align-items:center}
.help-text{font-size:16px;line-height:20px}
.help-text b{display:block;font-family:"Exo 2",sans-serif;font-size:22px;font-weight:500}
.lang{left:208px;top:21px;width:56px;height:34px;border:1px solid #fff;display:flex;align-items:center;justify-content:center;gap:5px}
.lang i{display:block;width:18px;height:12px;background:#fff}
.lang .caret{margin:0}
.advisor-tag{left:0;top:79px;width:282px;height:42px;background:var(--white);color:var(--ink);font-size:13px;text-align:center;line-height:42px;clip-path:polygon(12px 0,100% 0,calc(100% - 12px) 50%,100% 100%,12px 100%,0 50%)}
.lead-form{left:25px;top:140px;width:232px}
.lead-form h3{text-align:center;font-size:13px;font-weight:500;margin-bottom:13px}
.row{display:flex;gap:20px;margin-bottom:14px}
.field{flex:1;height:26px;background:#fff;color:#444;font-size:10px;padding-left:9px;line-height:26px;position:relative}
.field.sel::after{content:"";position:absolute;right:10px;top:11px;border:4px solid transparent;border-top-color:#222;border-bottom:0}
.search-btn{margin-top:7px;height:36px;border-radius:18px;background:var(--blue);color:#fff;text-align:center;line-height:36px;font-family:"Exo 2",sans-serif;font-size:16px;font-weight:500}

/* section titles */
.section-title{left:0;width:1200px;text-align:center;font-family:"Exo 2",sans-serif;font-size:28px;color:var(--blue)}
.rule{left:564px;width:72px;height:3px;display:flex;gap:4px}
.rule::before{content:"";flex:1;background:var(--blue)}
.rule::after{content:"";flex:1;background:var(--red)}
.lede{left:0;width:1200px;text-align:center;font-size:11px;line-height:17px;color:#222}

.features{left:118px;top:663px;width:966px;display:flex;justify-content:space-between}
.feature{width:180px;text-align:center}
.feature .disc{width:118px;height:118px;margin:0 auto;border-radius:50%;border:3px solid var(--blue);background:var(--red);outline:3px solid #fff;outline-offset:-6px;display:flex;align-items:center;justify-content:center;box-shadow:0 2px 6px rgba(0,0,0,.2)}
.feature p{margin-top:15px;font-size:13px;font-weight:500;line-height:18px}

.cost-band{left:0;top:908px;width:1200px;height:353px;background:linear-gradient(90deg,#3b3f2c 0%,#5a5a45 35%,#6f6450 60%,#4c4a3a 100%)}
.cost-title{left:0;top:972px;width:1200px;text-align:center;color:#fff;font-family:"Exo 2",sans-serif;font-size:27px}
.cost-copy{left:0;top:1042px;width:1200px;text-align:center;color:#eee;font-size:12px;line-height:19px;letter-spacing:.3px}
.cost-call{left:0;top:1108px;width:1200px;display:flex;justify-content:center;gap:10px;align-items:center;color:#fff;font-family:"Exo 2",sans-serif;font-size:20px}
.btn-contact{left:509px;top:1154px;width:182px;height:35px;border-radius:18px;background:var(--blue);color:#fff;font-family:"Exo 2",sans-serif;font-size:16px;display:flex;align-items:center;justify-content:center;gap:12px}

.info-card{top:1449px;width:283px;height:108px;border:1px solid #999;border-radius:4px;background:#fff}
.info-card svg{position:absolute;left:14px;top:14px}
.info-card h4{position:absolute;left:71px;top:18px;right:14px;font-size:14px;font-weight:500;line-height:20px}
.info-card p{position:absolute;left:71px;top:62px;right:14px;font-size:11px;line-height:17px;color:#444}

.advisor-search{left:353px;top:1600px;width:493px;height:34px;border:1px solid #aaa;border-radius:17px;overflow:hidden;display:flex}
.advisor-search span{flex:0 0 246px;line-height:32px;padding-left:41px;font-size:13px;color:#888}
.advisor-search b{flex:1;background:var(--blue);color:#fff;font-family:"Exo 2",sans-serif;font-weight:500;font-size:16px;line-height:32px;text-align:center}

.reviews{left:0;top:1704px;width:1200px;height:425px;background:var(--grey-bg)}
.quote{left:0;top:1848px;width:1200px;text-align:center;font-size:12px;font-style:italic;color:#444}
.who{left:0;top:1884px;width:1200px;text-align:center;font-size:11px;font-weight:600;color:#333}
.who-line{left:0;top:1908px;width:1200px;text-align:center;font-size:9px;color:#666}
.avatar{top:1945px;width:74px;height:74px;border-radius:8px;background:linear-gradient(#dfe3e6,#b8bec4)}
.avatar.current{border:4px solid var(--red);background:linear-gradient(#b9d6e6,#cfa98d)}
.dots{left:580px;top:2050px;display:flex;gap:6px}
.dots i{width:7px;height:7px;border-radius:50%;background:#ccc}
.dots i:first-child{background:var(--red)}

.states{left:140px;top:2286px;width:919px;height:385px;background:#fff;border-radius:6px;box-shadow:0 0 10px rgba(0,0,0,.12)}
.tabs{position:absolute;left:0;top:0;width:919px;height:54px;background:#f6f6f6;border-bottom:1px solid #eee}
.tab{position:absolute;top:0;height:54px;display:flex;align-items:center;justify-content:center;text-align:center;font-size:13px;font-weight:500;line-height:17px}
.tab.active{background:#fff;color:var(--red);border-radius:6px 6px 0 0;box-shadow:0 -2px 6px rgba(0,0,0,.08)}
.state-col{position:absolute;top:76px;font-size:12px;line-height:17px;color:#333;list-style:none}

.footer{left:0;top:2743px;width:1200px;height:128px;background:var(--black);color:#fff}
.foot-nav a{position:absolute;top:27px;color:#fff;font-size:12px;font-weight:500;text-decoration:none}
.foot-rule{left:141px;top:52px;width:671px;height:1px;background:#333}
.foot-info{position:absolute;top:75px;display:flex;gap:8px;font-size:11px;line-height:16px}
.foot-info .ring{flex:0 0 26px;height:26px;border-radius:50%;border:1px solid #fff;display:flex;align-items:center;justify-content:center;margin-top:3px}
.foot-info b{display:block;font-weight:600}
.foot-brand{left:878px;top:38px;color:#fff;font-family:"Exo 2",sans-serif;font-size:27px}
.foot-sub{left:878px;top:72px;width:181px;display:flex;align-items:center;gap:8px;font-size:11px}
.foot-sub::before,.foot-sub::after{content:"";flex:1;height:1px;background:#fff}
.copyright{left:0;top:2871px;width:1200px;height:33px;background:var(--red);color:#fff;font-size:12px}
.copyright p{position:absolute;left:141px;top:9px}
.social{position:absolute;top:4px;width:26px;height:26px;border-radius:50%;border:1px solid #fff}
</style>
</head>
<body>

<header class="abs site-header">
  <div class="abs brand">A Nook for Grandpas</div>
  <div class="abs brand-sub">Seniorcare Nonprofit</div>
</header>

<nav class="abs main-nav">
  <a class="active" style="left:141px">Assisted Living</a>
  <a style="left:296px">Memory Care</a>
  <a style="left:433px">Nursing Homes</a>
  <a style="left:585px">More Living Options<span class="caret"></span></a>
</nav>

<div class="abs hero" role="img" aria-label="Photo of a smiling senior couple"></div>

<aside class="abs lead-panel">
  <div class="abs help">
    <svg width="20" height="20" viewBox="0 0 24 24" fill="#fff"><path d="M6.6 10.8a15 15 0 0 0 6.6 6.6l2.2-2.2a1 1 0 0 1 1-.25 11.4 11.4 0 0 0 3.6.57 1 1 0 0 1 1 1V20a1 1 0 0 1-1 1A17 17 0 0 1 3 4a1 1 0 0 1 1-1h3.5a1 1 0 0 1 1 1c0 1.25.2 2.45.57 3.57a1 1 0 0 1-.25 1z"/></svg>
    <div class="help-text" style="margin-top:4px">Need help? Call<b>866-555-0147</b></div>
  </div>
  <div class="abs lang"><i></i><span class="caret"></span></div>
  <div class="abs advisor-tag">Talk to a local advisor for FREE</div>
  <div class="abs lead-form">
    <h3>Find Senior Living Near You.</h3>
    <div class="row"><div class="field">First Name</div><div class="field">Last Name</div></div>
    <div class="row"><div class="field">Phone Number</div></div>
    <div class="row"><div class="field">Email Address</div></div>
    <div class="row"><div class="field sel">Select State</div><div class="field sel">select City</div></div>
    <div class="row"><div class="field">Zip Code</div></div>
    <div class="search-btn">Start Your Search</div>
  </div>
</aside>

<h2 class="abs section-title" style="top:535px">The support you need to make the <span class="red">RIGHT CHOICE</span></h2>
<div class="abs rule" style="top:583px"></div>
<p class="abs lede" style="top:604px">Elder Nest Finder has already helped thousands of families find peace of<br>mind. Here's what's included with our free service:</p>

<div class="abs features">
  <div class="feature"><div class="disc"><svg width="48" height="54" viewBox="0 0 48 54" fill="#fff"><circle cx="24" cy="14" r="13"/><path d="M2 54c0-16 8-24 22-24s22 8 22 24z"/></svg></div><p>Dedicated local<br>advisor</p></div>
  <div class="feature"><div class="disc"><svg width="54" height="46" viewBox="0 0 54 46" fill="#fff"><path d="M27 2 2 24h7v22h14V32h8v14h14V24h7z"/></svg></div><p>Hand-picked list of<br>communities to match<br>your needs</p></div>
  <div class="feature"><div class="disc"><svg width="34" height="56" viewBox="0 0 34 56"><text x="17" y="48" text-anchor="middle" fill="#fff" font-family="Montserrat,sans-serif" font-weight="600" font-size="56">$</text></svg></div><p>Full details and<br>pricing</p></div>
  <div class="feature"><div class="disc"><svg width="50" height="50" viewBox="0 0 50 50" fill="none" stroke="#fff" stroke-width="3"><rect x="3" y="7" width="44" height="40" rx="3"/><path d="M3 17h44M14 2v9M36 2v9M3 27h44M3 37h44M14 17v30M25 17v30M36 17v30"/></svg></div><p>Help scheduling<br>tours</p></div>
  <div class="feature"><div class="disc"><svg width="56" height="42" viewBox="0 0 56 42" fill="#fff"><path d="M18 2h36v30H18zM2 16l6-10h8v26H2z"/><circle cx="12" cy="35" r="6" stroke="#e63b2e" stroke-width="3"/><circle cx="44" cy="35" r="6" stroke="#e63b2e" stroke-width="3"/></svg></div><p>Move in support</p></div>
</div>

<div class="abs cost-band" role="img" aria-label="Photo of a caregiver greeting a smiling senior woman"></div>
<h2 class="abs cost-title">There's no <span class="red">cost</span> to you.</h2>
<div class="abs rule" style="top:1020px;left:564px;width:34px;background:#fff;height:2px"></div>
<p class="abs cost-copy">We work with over 20,000 senior living communities.<br>Our community partners pay us for placement<br>services.</p>
<div class="abs cost-call">
  <svg width="20" height="20" viewBox="0 0 24 24" fill="#fff"><path d="M6.6 10.8a15 15 0 0 0 6.6 6.6l2.2-2.2a1 1 0 0 1 1-.25 11.4 11.4 0 0 0 3.6.57 1 1 0 0 1 1 1V20a1 1 0 0 1-1 1A17 17 0 0 1 3 4a1 1 0 0 1 1-1h3.5a1 1 0 0 1 1 1c0 1.25.2 2.45.57 3.57a1 1 0 0 1-.25 1z"/></svg>
  <span>Call866-555-0147</span>
</div>
<div class="abs btn-contact">Contact Now <svg width="18" height="16" viewBox="0 0 18 16" fill="#fff"><path d="M0 7 18 0 14 16 9 11 15 3 7 10z"/></svg></div>

<h2 class="abs section-title" style="top:1324px">Your <span class="red">LOCAL ADVISOR</span> informs. You decide.</h2>
<div class="abs rule" style="top:1372px"></div>
<p class="abs lede" style="top:1394px">Over 400 senior advisors across the U.S. and Canada are ready to help your family with:</p>

<div class="abs info-card" style="left:141px">
  <svg width="30" height="58" viewBox="0 0 30 58" fill="none" stroke="#e63b2e" stroke-width="2"><circle cx="15" cy="13" r="11"/><circle cx="13" cy="10" r="3"/><path d="M15 24v32"/></svg>
  <h4>Insider's tips for the area near you</h4>
  <p>Lorem ipsum dolor sit amet, consectetur adipiscing elit.</p>
</div>
<div class="abs info-card" style="left:458px">
  <svg width="46" height="42" viewBox="0 0 46 42" fill="none" stroke="#e63b2e" stroke-width="2"><path d="M23 40 4 21A11 11 0 0 1 23 7a11 11 0 0 1 19 14z"/></svg>
  <h4>Advice tailored to your unique situation</h4>
  <p>Lorem ipsum dolor sit amet, consectetur adipiscing elit.</p>
</div>
<div class="abs info-card" style="left:775px">
  <svg width="44" height="44" viewBox="0 0 44 44" fill="none" stroke="#e63b2e" stroke-width="2"><circle cx="22" cy="22" r="20"/><path d="M22 9v13H12"/></svg>
  <h4>Time saving know-how and resources</h4>
  <p>Lorem ipsum dolor sit amet, consectetur adipiscing elit.</p>
</div>

<div class="abs advisor-search"><span>Enter city or postal code</span><b>Find An Advisor Near You</b></div>

<section class="abs reviews"></section>
<h2 class="abs section-title" style="top:1769px"><span class="red">97%</span> of our customers recommend our service</h2>
<div class="abs rule" style="top:1816px"></div>
<p class="abs quote">“You were a great help. We really appreciate you &amp; Elder Nest Finder!”</p>
<p class="abs who">WALTER K</p>
<p class="abs who-line">Looking for Senior Living for his wife in Boise, ID</p>
<div class="abs avatar" style="left:455px" role="img" aria-label="Portrait of a senior man"></div>
<div class="abs avatar current" style="left:563px" role="img" aria-label="Portrait of a senior couple at the beach"></div>
<div class="abs avatar" style="left:671px" role="img" aria-label="Portrait of a senior woman"></div>
<div class="abs dots"><i></i><i></i><i></i></div>

<h2 class="abs section-title" style="top:2193px">Senior Living by <span class="red">State</span></h2>
<div class="abs rule" style="top:2240px"></div>

<div class="abs states">
  <div class="tabs">
    <div class="tab" style="left:0;width:116px">Memory<br>Care</div>
    <div class="tab active" style="left:105px;width:154px">Assisted<br>Living</div>
    <div class="tab" style="left:259px;width:152px">Independent<br>Living</div>
    <div class="tab" style="left:411px;width:108px">Nursing<br>Home</div>
    <div class="tab" style="left:519px;width:116px">Care<br>Homes</div>
  </div>
  <ul class="state-col" style="left:24px">
    <li>Alabama</li><li>Arizona</li><li>Arkansas</li><li>California</li><li>Colorado</li><li>Connecticut</li><li>Delaware</li><li>District of Columbia</li><li>Florida</li><li>Georgia</li><li>Hawaii</li><li>Idaho</li><li>Illinois</li><li>Indiana</li><li>Iowa</li><li>Kansas</li><li>Kentucky</li>
  </ul>
  <ul class="state-col" style="left:324px">
    <li>Louisiana</li><li>Maine</li><li>Maryland</li><li>Massachusetts</li><li>Michigan</li><li>Minnesota</li><li>Mississippi</li><li>Missouri</li><li>Montana</li><li>Nebraska</li><li>Nevada</li><li>New Hampshire</li><li>New Jersey</li><li>New Mexico</li><li>New York</li><li>North Carolina</li><li>North Dakota</li>
  </ul>
  <ul class="state-col" style="left:649px">
    <li>Ohio</li><li>Oklahoma</li><li>Oregon</li><li>Pennsylvania</li><li>Rhode Island</li><li>South Carolina</li><li>South Dakota</li><li>Tennessee</li><li>Texas</li><li>Utah</li><li>Vermont</li><li>Virginia</li><li>Washington</li><li>West Virginia</li><li>Wisconsin</li><li>Wyoming</li>
  </ul>
</div>

<footer class="abs footer">
  <nav class="foot-nav">
    <a style="left:141px">Assisted Living</a>
    <a style="left:278px">Memory Care</a>
    <a style="left:415px">Nursing Homes</a>
    <a style="left:567px">More Living Options<span class="caret"></span></a>
  </nav>
  <div class="abs foot-rule"></div>
  <div class="foot-info" style="left:182px">
    <span class="ring"><svg width="10" height="14" viewBox="0 0 10 14" fill="#2b4bd1"><path d="M5 0a5 5 0 0 1 5 5c0 4-5 9-5 9S0 9 0 5a5 5 0 0 1 5-5z"/></svg></span>
    <div><b>Address</b>48 Maple Row, Suite 210, Hartford,<br>CT 06103</div>
  </div>
  <div class="foot-info" style="left:471px">
    <span class="ring"><svg width="12" height="12" viewBox="0 0 24 24" fill="#2b4bd1"><path d="M6.6 10.8a15 15 0 0 0 6.6 6.6l2.2-2.2a1 1 0 0 1 1-.25 11.4 11.4 0 0 0 3.6.57 1 1 0 0 1 1 1V20a1 1 0 0 1-1 1A17 17 0 0 1 3 4a1 1 0 0 1 1-1h3.5a1 1 0 0 1 1 1c0 1.25.2 2.45.57 3.57a1 1 0 0 1-.25 1z"/></svg></span>
    <div><b>Call Us :</b>866-555-0147</div>
  </div>
  <div class="foot-info" style="left:617px">
    <span class="ring"><svg width="12" height="9" viewBox="0 0 12 9" fill="#2b4bd1"><rect width="12" height="9" rx="1"/></svg></span>
    <div><b>Email Us :</b>info@anookforgrandpas.net</div>
  </div>
  <div class="abs foot-brand">A Nook for Grandpas</div>
  <div class="abs foot-sub">Seniorcare Nonprofit</div>
</footer>

<div class="abs copyright">
  <p>Copyright 2019 A Nook for Grandpas Seniorcare Nonprofit . All Rights Reserved.</p>
  <span class="social" style="left:961px"></span>
  <span class="social" style="left:996px"></span>
  <span class="social" style="left:1032px"></span>
</div>

</body>
</html>
```